Adult Literacy Program - flyer to attract volunteers and students

We want a flyer that is engaging, colorful, modern and will appeal to our primary audience of adults aged 40-60. We are trying to attract both prospective volunteers (typically age 50+, mostly women) and students (typically aged 40+).
The flyer should feature diverse people working together in pairs of two, reading or talking, with a workbook or some reading material in front of them.

Our organization trains tutors to work one-on-one with adults who are learning how to read. Most of our adult students are non-native speakers of English. Many are of Haitian or Hispanic origin, so we would like some people who represent that demographic.

The Flyer should represent reading, learning, literacy, knowledge, growth,
and opportunities.
Our students are learning to read so they can advance their job opportunities.

Target Market(s)

Adults aged 40-60, primarily women, retired, volunteers

Industry/Entity Type

Education

Font styles to use
Serif
Sans Serif

Colors

Designer to choose colors to be used in the design.

Requirements
Must have
• - UPDATE: Should be designed as a TRI-FOLD brochure on 8.5 x 11 inch paper that will be folded into thirds.
• - Images of diverse people, women and men, who look Hispanic, Haitian and other nationalities as well as Caucasian.
• - Our logo on the front cover
Nice to have
• The sample flyer is very boring and dry! We are open to different ways of presenting the text.

```html
<!DOCTYPE html>
<html lang="en">
<head>
<meta charset="utf-8">
<title>Reading Circle Partners – Tri-fold Brochure</title>
<link rel="stylesheet" href="https://fonts.googleapis.com/css2?family=Montserrat:wght@500;700;800&family=Roboto+Slab:wght@400;500&family=Kalam:wght@400&display=swap">
<style>
  :root{
    --navy:#1b2461;
    --navy-deep:#141b4d;
    --cyan:#19aee5;
    --sky:#2a9fe0;
    --cloud:#e6e8ec;
    --paper:#ffffff;
    --silver:#c9cbcf;
    --ink:#1e2336;
    --bg:#d6d7d9;
  }
  *{box-sizing:border-box;margin:0;padding:0}
  html,body{width:837px;height:1200px;overflow:hidden;background:var(--bg)}
  body{position:relative;font-family:"Roboto Slab",serif;color:var(--ink)}
  .brochure{position:absolute;left:18px;top:289px;width:800px;height:622px;display:flex;box-shadow:0 6px 18px rgba(0,0,0,.18)}
  .panel{position:relative;width:266.67px;height:100%;overflow:hidden}
  .panel--inside{background:var(--paper)}
  .panel--contact{background:var(--navy)}
  .panel--cover{background:var(--paper)}
  .clouds{position:absolute;left:0;top:0;width:100%;height:140px}
  .brand-mark{position:absolute;left:50%;transform:translateX(-50%);display:flex;align-items:center;gap:6px;
    font-family:"Montserrat",sans-serif;font-weight:700;color:var(--navy);white-space:nowrap}
  .brand-mark .dot{width:10px;height:10px;border-radius:50%;background:var(--sky)}
  .pill{position:absolute;left:50%;transform:translateX(-50%);border-radius:20px;
    background:linear-gradient(#f4f4f5,#b9bbbf);text-align:center;color:var(--ink);white-space:nowrap}
  .pill--title{top:98px;width:180px;height:32px;line-height:32px;font-family:"Roboto Slab",serif;font-weight:500;font-size:15px;box-shadow:0 2px 3px rgba(0,0,0,.25)}
  .tutor-list{position:absolute;left:28px;top:152px;width:215px;list-style:none;font-size:10px;line-height:1.2}
  .tutor-list li{position:relative;padding-left:16px;margin-bottom:9px}
  .tutor-list svg{position:absolute;left:0;top:1px}
  .inside-headline{position:absolute;left:27px;top:278px;font-family:"Montserrat",sans-serif;font-weight:700;font-size:15.5px;line-height:1.2;color:var(--navy)}
  .inside-headline strong{display:block;font-size:24px;font-weight:800;color:var(--sky);letter-spacing:-.3px}
  .photo{position:absolute}
  .photo--tutoring{left:0;top:360px;width:100%;height:262px;background:linear-gradient(135deg,#6b4a3a,#b99a82 45%,#d9d2c8 70%,#8a5a52)}
  .panel-curve{position:absolute;left:0;width:100%}
  .contact-headline{position:absolute;top:38px;width:100%;text-align:center;font-family:"Montserrat",sans-serif;font-weight:700;font-size:26px;line-height:1.1;color:#fff}
  .contact-headline span{color:var(--cyan)}
  .pill--contact{top:110px;width:185px;height:22px;line-height:22px;font-size:11px}
  .script{font-family:"Kalam",cursive}
  .contact-title{position:absolute;top:158px;width:100%;text-align:center;font-size:21px;color:var(--cyan)}
  .contact-icons{position:absolute;top:194px;left:50%;transform:translateX(-50%);display:flex;gap:4px}
  .contact-details{position:absolute;top:214px;width:100%;text-align:center;font-family:"Montserrat",sans-serif;font-size:11px;line-height:1.4;color:#fff}
  .contact-details b{font-weight:700}
  .photo--mentor{left:33px;top:300px;width:200px;height:200px;border-radius:50%;background:linear-gradient(140deg,#d8c3ab,#e9a2a9 55%,#5b6f8f);border:6px solid #dfe1e4;box-shadow:0 0 0 2px #9fa2a8}
  .tagline-mark{position:absolute;top:530px;left:50%;transform:translateX(-50%);width:22px;height:22px;border-radius:50%;background:var(--navy)}
  .tagline{position:absolute;top:560px;width:100%;text-align:center;font-size:19px;color:var(--navy)}
  .brand-cover{position:absolute;top:118px;width:100%;text-align:center;font-family:"Montserrat",sans-serif;font-weight:700;color:var(--navy);font-size:17px;line-height:1.25;letter-spacing:1px}
  .brand-cover .dot{display:block;width:26px;height:26px;border-radius:50%;background:var(--sky);margin:0 auto 12px}
  .cover-tagline{position:absolute;top:168px;width:100%;text-align:center;font-size:18px;color:var(--navy)}
  .photo--pair{left:0;top:200px;width:100%;height:280px;background:linear-gradient(135deg,#c9b19b,#e8d6c6 40%,#9fb8d9 65%,#e9ecef)}
  .cover-title{position:absolute;top:500px;width:100%;text-align:center;font-family:"Roboto Slab",serif;font-size:30px;letter-spacing:1px;color:#fff}
  .cover-sub{position:absolute;top:530px;width:100%;text-align:center;font-size:28px;color:var(--cyan)}
  .pill--cover{top:573px;width:226px;height:21px;line-height:21px;font-size:9.5px}
  .cover-url{position:absolute;top:603px;width:100%;text-align:center;font-family:"Montserrat",sans-serif;font-size:7.5px;color:#fff;letter-spacing:.4px}
</style>
</head>
<body>
<main class="brochure">

  <section class="panel panel--inside">
    <svg class="clouds" viewBox="0 0 267 140" aria-hidden="true">
      <path d="M0 20 Q30 0 60 18 Q90 -2 120 20 Q150 0 180 20 Q215 2 240 22 Q258 10 267 18 V140 H0Z" fill="var(--cloud)"/>
      <path d="M0 50 Q40 40 80 52 Q130 38 180 52 Q230 40 267 50 V140 H0Z" fill="#f5f6f7"/>
    </svg>
    <div class="brand-mark" style="top:62px;font-size:12px"><span class="dot"></span>Reading Circle Partners</div>
    <div class="pill pill--title">TUTORS</div>
    <ul class="tutor-list">
      <li><svg width="10" height="10" viewBox="0 0 10 10"><circle cx="5" cy="5" r="5" fill="var(--navy)"/><path d="M2.6 5.2 4.3 6.8 7.4 3.4" stroke="#fff" stroke-width="1.4" fill="none"/></svg>No special skills or degrees needed just a degree of caring!</li>
      <li><svg width="10" height="10" viewBox="0 0 10 10"><circle cx="5" cy="5" r="5" fill="var(--navy)"/><path d="M2.6 5.2 4.3 6.8 7.4 3.4" stroke="#fff" stroke-width="1.4" fill="none"/></svg>Training offered throughout the year</li>
      <li><svg width="10" height="10" viewBox="0 0 10 10"><circle cx="5" cy="5" r="5" fill="var(--navy)"/><path d="M2.6 5.2 4.3 6.8 7.4 3.4" stroke="#fff" stroke-width="1.4" fill="none"/></svg>Tutors meet students weekly at a library</li>
      <li><svg width="10" height="10" viewBox="0 0 10 10"><circle cx="5" cy="5" r="5" fill="var(--navy)"/><path d="M2.6 5.2 4.3 6.8 7.4 3.4" stroke="#fff" stroke-width="1.4" fill="none"/></svg>Instructional materials provided</li>
      <li><svg width="10" height="10" viewBox="0 0 10 10"><circle cx="5" cy="5" r="5" fill="var(--navy)"/><path d="M2.6 5.2 4.3 6.8 7.4 3.4" stroke="#fff" stroke-width="1.4" fill="none"/></svg>Ongoing support available</li>
    </ul>
    <h2 class="inside-headline">TEACH AN ADULT TO READ<br>AND YOU’LL CHANGE A<strong>LIFE FOREVER.</strong></h2>
    <div class="photo photo--tutoring" role="img" aria-label="Photo of adult learners studying together at library tables"></div>
    <svg class="panel-curve" style="top:350px" height="40" viewBox="0 0 267 40" preserveAspectRatio="none" aria-hidden="true">
      <path d="M0 0 H267 V20 Q140 2 0 30Z" fill="#fff"/>
      <path d="M0 30 Q140 2 267 20" stroke="var(--silver)" stroke-width="4" fill="none"/>
    </svg>
  </section>

  <section class="panel panel--contact">
    <h2 class="contact-headline">DON’T WASTE<br><span>A MOMENT!</span></h2>
    <div class="pill pill--contact">Contact us today to learn more.</div>
    <h3 class="contact-title script">Contact Us</h3>
    <div class="contact-icons" aria-hidden="true">
      <svg width="12" height="12" viewBox="0 0 12 12"><circle cx="6" cy="6" r="6" fill="#fff"/><path d="M4 3.2 5 4.6 4.4 5.3Q5.2 6.9 6.7 7.6L7.4 7 8.8 8 8.2 9Q5 8.6 3 4Z" fill="var(--navy)"/></svg>
      <svg width="12" height="12" viewBox="0 0 12 12"><circle cx="6" cy="6" r="6" fill="#fff"/><rect x="3" y="4" width="6" height="4.2" fill="var(--navy)"/><path d="M3 4 6 6.4 9 4" stroke="#fff" stroke-width=".7" fill="none"/></svg>
    </div>
    <p class="contact-details"><b>Volunteer Desk</b> : 555-014-7510<br><b>Cedar Hollow, Millbrook &amp; Lakeview :</b><br>555-018-3453<br>tutors@readingcircle.org</p>
    <svg class="panel-curve" style="top:360px" height="262" viewBox="0 0 267 262" preserveAspectRatio="none" aria-hidden="true">
      <defs><linearGradient id="cyanFade" x1="0" y1="0" x2="0" y2="1"><stop offset="0" stop-color="#12a6e2"/><stop offset="1" stop-color="#5cd0f5"/></linearGradient></defs>
      <path d="M0 0 Q130 70 267 80 V262 H0Z" fill="url(#cyanFade)"/>
    </svg>
    <div class="photo photo--mentor" role="img" aria-label="Photo of a smiling volunteer tutor in a library"></div>
    <span class="tagline-mark" aria-hidden="true"></span>
    <p class="tagline script">Learning for life</p>
  </section>

  <section class="panel panel--cover">
    <svg class="clouds" viewBox="0 0 267 140" aria-hidden="true">
      <path d="M0 18 Q30 0 60 16 Q95 -2 130 18 Q165 0 200 18 Q235 2 267 16 V140 H0Z" fill="var(--cloud)"/>
      <path d="M0 55 Q50 42 100 56 Q160 40 210 55 Q240 46 267 52 V140 H0Z" fill="#f5f6f7"/>
    </svg>
    <h1 class="brand-cover" style="top:58px"><span class="dot"></span>READING CIRCLE<br>PARTNERS</h1>
    <p class="cover-tagline script">Learning for life</p>
    <div class="photo photo--pair" role="img" aria-label="Photo of a volunteer helping an older man at a laptop"></div>
    <svg class="panel-curve" style="top:440px" height="182" viewBox="0 0 267 182" preserveAspectRatio="none" aria-hidden="true">
      <path d="M0 30 Q130 0 267 20" stroke="var(--silver)" stroke-width="6" fill="none"/>
      <path d="M0 34 Q130 6 267 26 V182 H0Z" fill="var(--navy)"/>
    </svg>
    <h2 class="cover-title">VOLUNTEER</h2>
    <p class="cover-sub script">Enrich a Life!</p>
    <div class="pill pill--cover">Help an adult learn to read, write or speak English</div>
    <p class="cover-url">www.readingcircle.org</p>
  </section>

</main>
</body>
</html>
```